Web hosting and design company website

Hello
i need a website for my hosting company.
Brindle Peak Servers
http://brindlepeak.example
Should be technical, crisp, corporate and friendly.
needs a products page, contact, about us, portfolio
needs to be a wordpress site
Logo will be provided shortly
colours should be green, yello, blue, white, black

Industry/Entity Type

Information Technology

Coding

Coded - Design and coding required

Number of Pages Required

4 page

Font styles to use
Sans Serif

Colors
fbee3d
fbf289
acd036
cadf82
0692cd
33a6d7
0355a3
faa54b

Requirements
Must have
• about us
• contact us
• products
• portfolio

```html
<!DOCTYPE html>
<html lang="en">
<head>
<meta charset="utf-8">
<title>Brindle Peak Servers – Hosting &amp; Design</title>
<link rel="stylesheet" href="https://fonts.googleapis.com/css2?family=Lato:wght@400;700;900&family=Open+Sans:ital,wght@0,400;0,600;0,700;1,400&family=Roboto:wght@300;400&display=swap">
<style>
:root{
  --green:#a8cd37;
  --green-dark:#8fb22a;
  --blue:#1c93e3;
  --blue-deep:#0789c8;
  --navy:#2b4a6b;
  --ink:#222;
  --text:#555;
  --muted:#8a8a8a;
  --line:#e6e6e6;
  --panel:#f7f7f7;
  --white:#fff;
  --black:#0b0b0b;
}
*{box-sizing:border-box;margin:0;padding:0}
html,body{width:1200px;height:2293px;overflow:hidden}
body{position:relative;background:var(--white);font-family:"Open Sans",Arial,sans-serif;color:var(--text)}

/* header */
.site-header{position:absolute;left:0;top:0;width:1200px;height:95px;background:var(--white);border-bottom:1px solid #eee}
.brand{position:absolute;left:133px;top:29px;display:flex;align-items:center;gap:12px}
.brand-mark{width:40px;height:40px;border-radius:50%;background:var(--green)}
.brand-name{font-family:"Lato",sans-serif;font-size:25px;color:var(--ink)}
.main-nav{position:absolute;top:38px;left:0;width:1200px;font-family:"Roboto",sans-serif;font-size:14px;color:#444}
.main-nav a{position:absolute;color:inherit;text-decoration:none;white-space:nowrap}
.main-nav a.active{color:var(--green)}

/* hero */
.hero{position:absolute;left:0;top:95px;width:1200px;height:512px;background:linear-gradient(90deg,#f1f2f3 0%,#fafafa 45%,#eef0f2 100%)}
.hero-photo{position:absolute;left:658px;top:0;width:542px;height:512px;background:linear-gradient(160deg,#e9ecef 0%,#c9d7ea 45%,#7d9ccc 75%,#dfe3e8 100%)}
.hero-title{position:absolute;left:133px;top:100px;font-family:"Roboto",sans-serif;font-weight:300;font-size:43px;line-height:54px;color:var(--ink)}
.hero-name{position:absolute;left:133px;top:224px;font-family:"Lato",sans-serif;font-weight:700;font-size:41px;color:var(--ink);white-space:nowrap}
.hero-name span{color:var(--green)}
.hero-lead{position:absolute;left:133px;top:290px;width:520px;font-size:17px;line-height:28px;color:#333}
.hero-lead em{font-style:normal;color:var(--green)}
.btn-start{position:absolute;left:133px;top:367px;width:174px;height:46px;background:var(--green);color:#fff;font-size:12px;font-weight:600;display:flex;align-items:center;justify-content:center;letter-spacing:.3px}
.slider-dots{position:absolute;left:575px;top:466px;display:flex;gap:8px}
.slider-dots i{width:12px;height:12px;border-radius:50%;border:1.5px solid #333;display:block}
.slider-dots i.on{background:#333}

/* section headings */
.section-title{position:absolute;left:0;width:1200px;text-align:center;font-family:"Lato",sans-serif;font-weight:400;font-size:24px;color:var(--ink)}
.section-intro{position:absolute;left:0;width:1200px;text-align:center}

/* features */
.welcome-intro{top:700px;font-size:12px;line-height:21px;color:var(--muted)}
.feature{position:absolute;top:774px;width:217px;height:295px;background:#fbfbfb;border:1px solid #ededed;text-align:center}
.feature .icon{position:absolute;left:41px;top:24px;width:134px;height:134px;border-radius:50%;border:5px solid #eaeaea;display:flex;align-items:center;justify-content:center}
.feature .icon.blue{background:var(--blue-deep)}
.feature .icon.green{background:var(--green)}
.feature h3{position:absolute;top:188px;width:100%;font-family:"Lato",sans-serif;font-weight:400;font-size:17px;color:var(--ink)}
.feature p{position:absolute;top:216px;left:10px;right:10px;font-size:10px;line-height:17px;color:var(--muted)}

/* plans */
.plans{position:absolute;left:0;top:1128px;width:1200px;height:568px;background:var(--panel)}
.plans-intro{top:1216px;font-size:17px;color:#555}
.plan{position:absolute;top:1275px;width:240px;text-align:center}
.plan h3{font-family:"Open Sans",sans-serif;font-weight:600;font-size:28px;line-height:36px}
.plan small{display:block;font-size:10px;color:var(--muted);margin-top:-3px}
.plan .box{position:absolute;top:60px;left:0;width:240px;height:298px;background:#fff;border:1px solid #ddd}
.plan .price{height:46px;display:flex;align-items:center;justify-content:center;font-weight:700;font-size:24px;border-bottom:4px solid #777;position:relative}
.plan .price sub{font-size:12px;vertical-align:baseline;margin-left:1px}
.plan .price::after{content:"";position:absolute;left:112px;bottom:-12px;border:8px solid transparent;border-top-color:#777;border-bottom:0}
.plan ul{list-style:none;text-align:left;padding:26px 0 0 34px}
.plan li{font-size:12.5px;color:#444;height:29px;display:flex;align-items:center;gap:9px}
.plan li svg{flex:none}
.plan .order{position:absolute;left:-1px;bottom:-1px;width:240px;height:35px;color:#fff;font-weight:700;font-size:13px;display:flex;align-items:center;justify-content:center}
.plan.simple h3,.plan.expert h3{color:var(--navy)}
.plan.simple .price,.plan.expert .price{color:var(--blue)}
.plan.simple .order,.plan.expert .order{background:var(--blue)}
.plan.starter h3{color:var(--green)}
.plan.starter .price{color:var(--green);border-bottom-color:var(--green)}
.plan.starter .price::after{border-top-color:var(--green)}
.plan.starter .order{background:var(--green)}

/* testimonial */
.testimonial{position:absolute;left:0;top:1696px;width:1200px;height:270px;background:var(--green)}
.testimonial h2{position:absolute;top:45px;width:100%;text-align:center;font-family:"Lato",sans-serif;font-weight:400;font-size:25px;color:#fff}
.avatar{position:absolute;left:179px;top:93px;width:132px;height:132px;border-radius:50%;border:5px solid #fff;background:linear-gradient(180deg,#e8e8e8 0%,#b9b9b9 55%,#5d6470 100%)}
.quote{position:absolute;left:347px;top:100px;width:682px;font-style:italic;font-size:12px;line-height:20px;color:#fff}
.quote-author{position:absolute;left:347px;top:197px;font-size:15px;font-weight:700;color:#fff}
.quote-author span{font-weight:400;font-size:12px}
.arrow{position:absolute;top:137px}

/* clients */
.clients-intro{top:2046px;font-size:18px;color:#444}
.client{position:absolute;top:2090px;height:70px;display:flex;align-items:center;gap:9px;font-family:"Open Sans",sans-serif;font-size:22px;color:#333;white-space:nowrap}
.client i{display:block;width:22px;height:22px;background:#333;flex:none}
.client.first{background:#f4f4f4;padding:0 10px;height:90px;top:2078px}

/* footer */
.site-footer{position:absolute;left:0;top:2173px;width:1200px;height:120px;background:var(--black);color:#bbb;font-size:12px}
.foot-links{position:absolute;left:133px;top:45px;color:#ccc}
.foot-copy{position:absolute;left:133px;top:69px;color:#999}
.news-label{position:absolute;left:433px;top:41px;color:#ddd;font-size:11px}
.news-form{position:absolute;left:433px;top:62px;display:flex}
.news-form .field{width:143px;height:22px;background:#d9d9d9;color:#888;font-size:10px;padding:5px 8px}
.news-form .go{width:61px;height:22px;background:#6a8f1a;color:#fff;font-size:10px;display:flex;align-items:center;justify-content:center}
.call{position:absolute;left:712px;top:40px;display:flex;gap:10px;align-items:center}
.call small{display:block;font-size:12px;color:#888}
.call strong{display:block;font-weight:400;font-size:20px;color:#ccc;line-height:22px}
.social{position:absolute;left:940px;top:45px;display:flex;gap:10px}
.social i{display:block;width:27px;height:27px;border-radius:50%;background:#444}
</style>
</head>
<body>

<header class="site-header">
  <div class="brand"><span class="brand-mark"></span><span class="brand-name">Brindle Peak Servers</span></div>
  <nav class="main-nav">
    <a class="active" style="left:626px">Home</a>
    <a style="left:707px">About us</a>
    <a style="left:806px">Products</a>
    <a style="left:905px">Portfolio</a>
    <a style="left:1002px">Contact us</a>
  </nav>
</header>

<section class="hero">
  <div class="hero-photo" role="img" aria-label="Smiling woman with glasses in a blue shirt working on a laptop in a bright office"></div>
  <h1 class="hero-title">Your Trusted &amp; Reliable<br>hosting &amp; design</h1>
  <div class="hero-name">BRINDLE PEAK <span>SERVERS</span></div>
  <p class="hero-lead">Powerful and Cheap web hosting and domains for your website get web hosting and receive a <em>FREE Domain Name !</em></p>
  <div class="btn-start">GET STARTED NOW !</div>
  <div class="slider-dots"><i></i><i class="on"></i><i></i></div>
</section>

<h2 class="section-title" style="top:655px">Welcome to Brindle Peak Servers</h2>
<p class="section-intro welcome-intro">Lorem ipsum dolor sit amet, consectetur adipiscing elit, sed do eiusmod tempor incididunt ut labore et dolore magna aliqua. Ut enim ad minim veniam,<br>quis nostrud exercitation ullamco laboris nisi ut aliquip ex ea commodo</p>

<div class="feature" style="left:131px">
  <div class="icon blue">
    <svg width="64" height="50" viewBox="0 0 64 50"><path d="M6 44 A28 28 0 1 1 58 44 Z" fill="#fff"/><circle cx="32" cy="34" r="5" fill="#0789c8"/><path d="M32 34 L44 18" stroke="#0789c8" stroke-width="4" stroke-linecap="round"/><g fill="#0789c8"><circle cx="14" cy="32" r="2.5"/><circle cx="19" cy="19" r="2.5"/><circle cx="32" cy="13" r="2.5"/><circle cx="50" cy="32" r="2.5"/></g></svg>
  </div>
  <h3>Optimized Software</h3>
  <p>Lorem ipsum dolor sit amet, nsectetur adipiscing elit, sed do eiusmod tempor incididunt ut labore et dolore</p>
</div>
<div class="feature" style="left:375px">
  <div class="icon green">
    <svg width="60" height="56" viewBox="0 0 60 56"><rect x="8" y="4" width="32" height="40" fill="#fff" stroke="#a8cd37" stroke-width="2"/><rect x="14" y="10" width="32" height="40" fill="#fff" stroke="#a8cd37" stroke-width="2"/><rect x="4" y="22" width="52" height="32" rx="2" fill="#fff"/><rect x="23" y="36" width="14" height="12" fill="#a8cd37"/><path d="M25 36 v-4 a5 5 0 0 1 10 0 v4" fill="none" stroke="#a8cd37" stroke-width="2.5"/></svg>
  </div>
  <h3>Account Isolation</h3>
  <p>Lorem ipsum dolor sit amet, nsectetur adipiscing elit, sed do eiusmod tempor incididunt ut labore et dolore</p>
</div>
<div class="feature" style="left:608px">
  <div class="icon blue">
    <svg width="60" height="56" viewBox="0 0 60 56"><path d="M4 24 h16 l4 5 h32 v25 h-52 z" fill="#fff"/><path d="M30 2 v22 M21 15 l9 9 l9 -9" stroke="#fff" stroke-width="5" fill="none" stroke-linejoin="round"/></svg>
  </div>
  <h3>Daily Backups</h3>
  <p>Lorem ipsum dolor sit amet, nsectetur adipiscing elit, sed do eiusmod tempor incididunt ut labore et dolore</p>
</div>
<div class="feature" style="left:851px">
  <div class="icon blue">
    <svg width="70" height="48" viewBox="0 0 70 48"><path d="M16 46 a14 14 0 0 1 0 -28 a20 20 0 0 1 38 4 a12 12 0 0 1 0 24 z" fill="#fff"/><path d="M35 38 v-16 M27 29 l8 -8 l8 8" stroke="#0789c8" stroke-width="5" fill="none"/></svg>
  </div>
  <h3>Edgeshield Integration</h3>
  <p>Lorem ipsum dolor sit amet, nsectetur adipiscing elit, sed do eiusmod tempor incididunt ut labore et dolore</p>
</div>

<section class="plans"></section>
<h2 class="section-title" style="top:1177px">Most Popular Hosting Plans</h2>
<p class="section-intro plans-intro">Choose the high-touch service level that's right for your business needs.</p>

<div class="plan simple" style="left:196px">
  <h3>Simple</h3><small>Customer recommended</small>
  <div class="box">
    <div class="price">£15<sub>/month</sub></div>
    <ul>
      <li><svg width="10" height="9"><path d="M1 5 l3 3 l5 -7" stroke="#444" stroke-width="2" fill="none"/></svg>Cloud Engineers available</li>
      <li><svg width="10" height="9"><path d="M1 5 l3 3 l5 -7" stroke="#444" stroke-width="2" fill="none"/></svg>Architecture advisors</li>
      <li><svg width="10" height="9"><path d="M1 5 l3 3 l5 -7" stroke="#444" stroke-width="2" fill="none"/></svg>Security guidance</li>
      <li><svg width="10" height="9"><path d="M1 5 l3 3 l5 -7" stroke="#444" stroke-width="2" fill="none"/></svg>Support SLA</li>
      <li><svg width="10" height="9"><path d="M1 5 l3 3 l5 -7" stroke="#444" stroke-width="2" fill="none"/></svg>Migration support</li>
      <li><svg width="10" height="9"><path d="M1 5 l3 3 l5 -7" stroke="#444" stroke-width="2" fill="none"/></svg>Reporting dashboard</li>
    </ul>
    <div class="order">ORDER NOW</div>
  </div>
</div>
<div class="plan starter" style="left:481px">
  <h3>Starter</h3><small>Customer recommended</small>
  <div class="box">
    <div class="price">£20<sub>/month</sub></div>
    <ul>
      <li><svg width="10" height="9"><path d="M1 5 l3 3 l5 -7" stroke="#444" stroke-width="2" fill="none"/></svg>Cloud Engineers available</li>
      <li><svg width="10" height="9"><path d="M1 5 l3 3 l5 -7" stroke="#444" stroke-width="2" fill="none"/></svg>Architecture advisors</li>
      <li><svg width="10" height="9"><path d="M1 5 l3 3 l5 -7" stroke="#444" stroke-width="2" fill="none"/></svg>Security guidance</li>
      <li><svg width="10" height="9"><path d="M1 5 l3 3 l5 -7" stroke="#444" stroke-width="2" fill="none"/></svg>Support SLA</li>
      <li><svg width="10" height="9"><path d="M1 5 l3 3 l5 -7" stroke="#444" stroke-width="2" fill="none"/></svg>Migration support</li>
      <li><svg width="10" height="9"><path d="M1 5 l3 3 l5 -7" stroke="#444" stroke-width="2" fill="none"/></svg>Reporting dashboard</li>
    </ul>
    <div class="order">ORDER NOW</div>
  </div>
</div>
<div class="plan expert" style="left:764px">
  <h3>Expert</h3><small>Customer recommended</small>
  <div class="box">
    <div class="price">£25<sub>/month</sub></div>
    <ul>
      <li><svg width="10" height="9"><path d="M1 5 l3 3 l5 -7" stroke="#444" stroke-width="2" fill="none"/></svg>Cloud Engineers available</li>
      <li><svg width="10" height="9"><path d="M1 5 l3 3 l5 -7" stroke="#444" stroke-width="2" fill="none"/></svg>Architecture advisors</li>
      <li><svg width="10" height="9"><path d="M1 5 l3 3 l5 -7" stroke="#444" stroke-width="2" fill="none"/></svg>Security guidance</li>
      <li><svg width="10" height="9"><path d="M1 5 l3 3 l5 -7" stroke="#444" stroke-width="2" fill="none"/></svg>Support SLA</li>
      <li><svg width="10" height="9"><path d="M1 5 l3 3 l5 -7" stroke="#444" stroke-width="2" fill="none"/></svg>Migration support</li>
      <li><svg width="10" height="9"><path d="M1 5 l3 3 l5 -7" stroke="#444" stroke-width="2" fill="none"/></svg>Reporting dashboard</li>
    </ul>
    <div class="order">ORDER NOW</div>
  </div>
</div>

<section class="testimonial">
  <h2>Whats our customer say about us</h2>
  <svg class="arrow" style="left:119px" width="16" height="28" viewBox="0 0 16 28"><path d="M13 2 L3 14 L13 26" stroke="#7f9e26" stroke-width="3" fill="none"/></svg>
  <div class="avatar" role="img" aria-label="Portrait photo of a businessman in a suit"></div>
  <p class="quote">" Lorem ipsum dolor sit amet, consectetur adipiscing elit, sed do eiusmod tempor incididunt ut labore et dolore magna aliqua. Ut enim ad minim veniam, quis nostrud exercitation ullamco laboris nisi ut aliquip ex ea commodo consequat. Duis aute irure dolor in reprehenderit in voluptate velit esse cillum dolore eu fugiat nulla pariatur. Excepteur sint occaecat cupidatat non proidentre prehenderit in voluptate velit esse cillum dolore eu fugiat nulla pariatur "</p>
  <div class="quote-author">Daniel Marsh,<span>Manager</span></div>
  <svg class="arrow" style="left:1065px" width="16" height="28" viewBox="0 0 16 28"><path d="M3 2 L13 14 L3 26" stroke="#7f9e26" stroke-width="3" fill="none"/></svg>
</section>

<h2 class="section-title" style="top:2008px">Our Clients</h2>
<p class="section-intro clients-intro">Lorem ipsum dolor sit amet, consectetur adipiscing elit, sed do eiusmod</p>
<div class="client first" style="left:172px"><i style="border-radius:50%"></i>Loremworks</div>
<div class="client" style="left:372px"><i></i>Northwind Labs</div>
<div class="client" style="left:612px"><i></i>Grainfield</div>
<div class="client" style="left:818px"><i style="border-radius:50%"></i>Layoutcraft</div>

<footer class="site-footer">
  <div class="foot-links">About &nbsp;|&nbsp; Terms &nbsp;|&nbsp; Privacy Policy</div>
  <div class="foot-copy">All Rights Reserved. Copyrights © 2015.</div>
  <div class="news-label">Newsletter Signup</div>
  <div class="news-form"><div class="field">Email Address</div><div class="go">Subscribe</div></div>
  <div class="call">
    <svg width="34" height="34" viewBox="0 0 34 34"><circle cx="17" cy="17" r="15.5" fill="none" stroke="#777" stroke-width="2"/><path d="M11 9 l4 0 l1.5 5 l-2.5 2 q2 4 5 5 l2 -2.5 l5 1.5 l0 4 q-1 2 -4 1.5 q-11 -3 -13 -13 q0 -3 2 -3.5z" fill="#777"/></svg>
    <div><small>Call Us:</small><strong>01-555-01234</strong></div>
  </div>
  <div class="social"><i></i><i></i><i></i><i></i></div>
</footer>

</body>
</html>
```